Maple Bug Guard Business Cards

A modern business card with a predominantly white background and a sleek design featuring Maple with complimentary greys or blacks to convey a professional and contemporary look.

Front:
Primarily white background. Limited use of company purple color can be neighbored by greys.
Text: Name, Title, Cell Phone, Office Phone, Website, email address

Back:
Background Continuation: The back of the card maintains the white background for consistency.
Company name “Maple” in company color and font, “Bug Guard” underneath or underneath left justified of “Maple.”
A subtle pattern or texture in shades of grey to add depth behind the company Logo in font.

logo color: hex #6212ab
font: antique olive nord D Regular

```html
<!DOCTYPE html>
<html lang="en">
<head>
<meta charset="UTF-8">
<title>Maple Bug Guard Business Cards</title>
<link href="https://fonts.googleapis.com/css2?family=Montserrat:wght@400;500;800&display=swap" rel="stylesheet">
<style>
  :root {
    --brand: #6212ab;
    --band: #7416b2;
    --rule: #8c8c8c;
    --ink: #3a3a3a;
    --paper: #ffffff;
    --backdrop: #3b3b3d;
  }
  * { box-sizing: border-box; margin: 0; padding: 0; }
  html, body { width: 1200px; height: 1200px; overflow: hidden; }
  body {
    background: var(--backdrop);
    font-family: "Montserrat", Arial, sans-serif;
    position: relative;
  }
  .card {
    position: absolute;
    width: 700px;
    height: 400px;
    border-radius: 30px;
    background: var(--paper);
    overflow: hidden;
    box-shadow: 0 12px 28px rgba(0,0,0,0.35);
  }
  .card--front { left: 90px; top: 110px; }
  .card--back { left: 410px; top: 690px; }

  .wordmark { position: absolute; color: var(--brand); font-weight: 800; line-height: 0.95; }
  .wordmark__main { display: block; letter-spacing: -2px; }
  .wordmark__sub { display: block; letter-spacing: 6px; text-transform: uppercase; }

  .card--front .wordmark { left: 150px; top: 42px; }
  .card--front .wordmark__main { font-size: 112px; }
  .card--front .wordmark__sub { font-size: 22px; margin-top: 4px; padding-left: 6px; }

  .card--back .wordmark { left: 140px; top: 98px; }
  .card--back .wordmark__main { font-size: 150px; }
  .card--back .wordmark__sub { font-size: 28px; margin-top: 6px; padding-left: 8px; }

  .front__rule {
    position: absolute; left: 0; right: 0; top: 222px; height: 7px;
    background: var(--rule);
  }
  .front__band {
    position: absolute; left: 0; right: 0; top: 236px; bottom: 0;
    background: var(--band);
    color: var(--paper);
  }
  .person { position: absolute; left: 70px; top: 56px; }
  .person__name { font-size: 34px; font-weight: 500; letter-spacing: -0.5px; }
  .person__title { font-size: 18px; font-weight: 400; margin-top: 2px; padding-left: 12px; }

  .contacts { position: absolute; left: 390px; top: 22px; list-style: none; }
  .contacts li {
    display: flex; align-items: center; gap: 10px;
    font-size: 19px; font-weight: 400; height: 30px;
  }
  .contacts svg { width: 18px; height: 18px; flex: none; }
</style>
</head>
<body>

<section class="card card--front" aria-label="Business card front">
  <div class="wordmark">
    <span class="wordmark__main">Maple</span>
    <span class="wordmark__sub">Bug Guard</span>
  </div>
  <div class="front__rule"></div>
  <div class="front__band">
    <div class="person">
      <p class="person__name">FULL NAME</p>
      <p class="person__title">TITLE</p>
    </div>
    <ul class="contacts">
      <li>
        <svg viewBox="0 0 18 18" aria-hidden="true"><rect x="4.5" y="1" width="9" height="16" rx="1.5" fill="none" stroke="#fff" stroke-width="1.5"/><circle cx="9" cy="14" r="1" fill="#fff"/></svg>
        555-310-4826
      </li>
      <li>
        <svg viewBox="0 0 18 18" aria-hidden="true"><path d="M4 1.5l3 3-1.6 2.2a10 10 0 0 0 5.9 5.9L13.5 11l3 3-2 2.5C8 16 2 10 1.5 3.5z" fill="#fff"/></svg>
        555-310-4827
      </li>
      <li>
        <svg viewBox="0 0 18 18" aria-hidden="true"><g fill="none" stroke="#fff" stroke-width="1.3"><circle cx="9" cy="9" r="7.5"/><ellipse cx="9" cy="9" rx="3.3" ry="7.5"/><path d="M1.5 9h15M3 5h12M3 13h12"/></g></svg>
        www.maplebugguard.com
      </li>
      <li>
        <svg viewBox="0 0 18 18" aria-hidden="true"><rect x="1" y="3.5" width="16" height="11" fill="#fff"/><path d="M1 3.5l8 6 8-6M1 14.5l6-5M17 14.5l-6-5" fill="none" stroke="#7416b2" stroke-width="1.2"/></svg>
        hello@maplebugguard.com
      </li>
    </ul>
  </div>
</section>

<section class="card card--back" aria-label="Business card back">
  <div class="wordmark">
    <span class="wordmark__main">Maple</span>
    <span class="wordmark__sub">Bug Guard</span>
  </div>
</section>

</body>
</html>
```